Security Company Needs an UPDATED Business Card and Letterhead Design!

I run a security company and would like to have an updated BUSINESS CARD + LETTERHEAD DESIGN.

Please use my UPDATED address below:

2875 E. Thornwick Road
Suite 614 Dallas, Texas 75390

Attached is the current business card as reference, and also my logo.

Target Market(s)

High end security users such as Class A buildings, Corporate Campus Locations, Hospitals, High End Retail Centers, Warehousing, Manufacturing and High Tech Companies

Industry/Entity Type

Security Guard

Contact Information for Business Card

Looking for unique, yet professional

Requirements
Must have
• Must use the current logo and incorporate it into any design. Use the colors that are included in the logo. I also need to be able to easily add employees as the company grows. Should be an easy process to change Names and Numbers

```html
<!DOCTYPE html>
<html lang="en">
<head>
<meta charset="utf-8">
<title>Harlow Guard Group – Business Card</title>
<link href="https://fonts.googleapis.com/css2?family=Roboto+Condensed:wght@400;700&display=swap" rel="stylesheet">
<style>
  :root {
    --navy: #2c2f92;
    --navy-deep: #1f2270;
    --grey-text: #8b8c92;
    --grey-icon: #b3b4b8;
    --rule: #a9aaae;
    --card: #fbfbfb;
    --backdrop: #e6e4e0;
  }
  * { margin: 0; padding: 0; box-sizing: border-box; }
  html, body {
    width: 1200px; height: 780px; overflow: hidden;
    background: var(--backdrop);
    font-family: "Roboto Condensed", "Arial Narrow", sans-serif;
  }
  .card {
    position: absolute; left: 75px; top: 90px;
    width: 1050px; height: 600px;
    background: linear-gradient(135deg, #ffffff 0%, var(--card) 55%, #f1f1f2 100%);
    box-shadow: 0 18px 40px rgba(0,0,0,.18);
  }
  .social {
    position: absolute; top: 52px; right: 60px;
    display: flex; gap: 16px;
  }
  .social-tile {
    width: 38px; height: 38px; border-radius: 4px;
    background: var(--grey-icon);
  }
  .brand {
    position: absolute; left: 70px; top: 215px;
    display: flex; align-items: center; gap: 18px;
  }
  .brand-dot {
    width: 64px; height: 64px; border-radius: 50%;
    background: var(--navy);
  }
  .brand-name {
    font-weight: 700; font-size: 30px; line-height: 1.05;
    letter-spacing: 2px; color: var(--navy); text-transform: uppercase;
  }
  .person {
    position: absolute; left: 470px; top: 170px;
  }
  .person-name {
    font-weight: 700; font-size: 46px; letter-spacing: 1px;
    color: var(--navy); text-transform: uppercase;
  }
  .person-title {
    font-size: 28px; color: var(--grey-text); margin-top: 4px;
  }
  .divider {
    position: absolute; left: 70px; right: 60px; top: 330px;
    height: 2px; background: var(--rule);
  }
  .contact {
    position: absolute; left: 70px; top: 370px;
    list-style: none;
  }
  .contact li {
    display: flex; align-items: center; gap: 16px;
    font-size: 30px; color: var(--grey-text);
    margin-bottom: 14px;
  }
  .contact-icon {
    width: 34px; height: 34px; border-radius: 3px;
    background: var(--navy); flex: none;
  }
  .address {
    position: absolute; left: 640px; top: 370px;
    font-style: normal; font-size: 30px; line-height: 1.45;
    color: var(--grey-text);
  }
</style>
</head>
<body>
  <section class="card">
    <div class="social" aria-label="Social profiles">
      <span class="social-tile"></span>
      <span class="social-tile"></span>
      <span class="social-tile"></span>
      <span class="social-tile"></span>
    </div>

    <div class="brand">
      <span class="brand-dot"></span>
      <span class="brand-name">Harlow<br>Guard Group</span>
    </div>

    <div class="person">
      <h1 class="person-name">Daniel R. Whitcombe</h1>
      <p class="person-title">President &amp; CEO</p>
    </div>

    <div class="divider"></div>

    <ul class="contact">
      <li>
        <svg class="contact-icon" viewBox="0 0 34 34" aria-hidden="true">
          <rect width="34" height="34" rx="3" fill="var(--navy)"/>
          <path d="M11 8h4l2 5-3 2c1 3 3 5 6 6l2-3 5 2v4c0 1-1 2-2 2C15 26 8 19 8 10c0-1 1-2 3-2z" fill="#fff"/>
        </svg>
        <span>602-555-0174</span>
      </li>
      <li>
        <svg class="contact-icon" viewBox="0 0 34 34" aria-hidden="true">
          <rect width="34" height="34" rx="3" fill="var(--navy)"/>
          <rect x="7" y="10" width="20" height="14" fill="none" stroke="#fff" stroke-width="2"/>
          <path d="M7 10l10 8 10-8" fill="none" stroke="#fff" stroke-width="2"/>
        </svg>
        <span>dan@harlowguard.com</span>
      </li>
      <li>
        <svg class="contact-icon" viewBox="0 0 34 34" aria-hidden="true">
          <rect width="34" height="34" rx="3" fill="var(--navy)"/>
          <circle cx="17" cy="17" r="10" fill="none" stroke="#fff" stroke-width="2"/>
          <ellipse cx="17" cy="17" rx="4.5" ry="10" fill="none" stroke="#fff" stroke-width="1.6"/>
          <path d="M7 17h20M9 12h16M9 22h16" stroke="#fff" stroke-width="1.6"/>
        </svg>
        <span>www.harlowguardgroup.com</span>
      </li>
    </ul>

    <address class="address">
      2875 E. Thornwick Road<br>
      Suite 614 Dallas<br>
      Texas 75390
    </address>
  </section>
</body>
</html>
```